NO MORE DESIGNS PLEASE."OPENING SOON' brochure for KESTRELVALE CELLS Pty Ltd .

Kestrelvale Cells is a locally owed and operated company. We provide a quality range of batteries (Marlow LiFeP04 and Tidebrook). From traditional sealed lead acid batteries, the latest AGM technologies and Lithium iron phosphate (LiFeP04).Our Suppliers have been in the manufacturing and battery industry for over 40 years. We wholesale and retail from a modern warehouse in Butler WA. We supply batteries for most applications including , Automotive, Critical power, Fire and Security, Mobility, Marine, Powersport, Motorcycle, Recreation, and truck and Tractor. All our Lithium iron phosphate (LiFeP04) batteries are IEC certified which sets us apart from other inferior products on the market. We are a start up business and new to the area. This brochure is to let people know we are opening soon, where we are and what we do.As part of our service we offer free delivery free battery testing and diagnosis and free installation. WE HAVE 3 DESIGNS WE ARE CHOOSING FROM FOR OUR WINNER. THANKYOU TO ALL THE TALENTED DESIGNERS THAT HAVE BLESSED US WITH THERE CREATIONS. IT IS VERY DIFFICULT TO TURN AWAY SUCH FANTASTIC TALENT. WE CAN ONLY CHOOSE ONE . THANKYOU FOR UNDERSTANDING.

Target Market(s)

18-65

Industry/Entity Type

Automotive

Font styles to use
Sans Serif

Colors
0392cd
f5f5f5
b1b1b1

Requirements
Must have
• WE HAVE 3 DESIGNS WE ARE CHOOSING FROM FOR OUR WINNER. THANKYOU TO ALL THE TALENTED DESIGNERS THAT HAVE BLESSED US WITH THERE CREATIONS. IT IS VERY DIFFICULT TO TURN AWAY SUCH FANTASTIC TALENT. WE CAN ONLY ONE. THANKYOU FOR UNDERSTANDING.
Nice to have
• Some wow factor
Should not have
• Boxes and lines

```html
<!DOCTYPE html>
<html lang="en">
<head>
<meta charset="utf-8">
<title>Kestrelvale Cells – Opening Soon</title>
<link href="https://fonts.googleapis.com/css2?family=Anton&family=Montserrat:wght@400;500;700;800&family=Oswald:wght@600&display=swap" rel="stylesheet">
<style>
  :root {
    --brand-blue: #0392cd;
    --deep-blue: #0d55a5;
    --ink-blue: #1a5db4;
    --light: #f5f5f5;
    --grey: #b1b1b1;
    --icon-grey: #a7a7a7;
    --line-grey: #9a9a9a;
    --sky-edge: #bcd6e2;
    --sky-centre: #f1f7fa;
  }
  * { margin: 0; padding: 0; box-sizing: border-box; }
  html, body { width: 1200px; height: 1200px; overflow: hidden; background: #ffffff; }
  .canvas { position: relative; width: 1200px; height: 1200px; }

  .brochure {
    position: absolute; left: 182px; top: 58px; width: 836px; height: 1084px;
    background: radial-gradient(ellipse 62% 55% at 50% 58%, var(--sky-centre) 0%, #dcebf2 55%, var(--sky-edge) 100%);
    overflow: hidden;
  }

  .brand-mark {
    position: absolute; left: 0; right: 0; top: 372px;
    display: flex; align-items: center; justify-content: center; gap: 14px;
  }
  .brand-mark .badge { width: 40px; height: 40px; background: var(--ink-blue); }
  .brand-mark .name {
    font-family: "Montserrat", sans-serif; font-weight: 800; font-size: 38px;
    letter-spacing: 1px; color: var(--ink-blue);
  }

  .headline {
    position: absolute; left: 0; right: 0; top: 486px; text-align: center;
    font-family: "Anton", sans-serif; font-weight: 400; font-size: 96px; line-height: 1;
  }
  .headline span {
    display: inline-block; letter-spacing: 3px; color: var(--brand-blue);
    text-shadow: 5px 5px 0 var(--grey);
    transform: scaleX(1.15);
  }

  .contact-label {
    position: absolute; left: 82px; bottom: 6px;
    transform-origin: left bottom; transform: rotate(-90deg);
    font-family: "Oswald", sans-serif; font-weight: 600; font-size: 44px; line-height: 1;
    color: var(--light);
    white-space: nowrap;
  }

  .card-front {
    position: absolute; left: 124px; top: 875px; width: 356px; height: 209px;
    background: #ffffff; font-family: "Montserrat", sans-serif; color: var(--ink-blue);
  }
  .card-front .person { position: absolute; left: 20px; top: 38px; font-weight: 800; font-size: 14px; }
  .card-front .mini-brand { position: absolute; right: 18px; top: 38px; font-weight: 800; font-size: 12.5px; }
  .card-front .rule { position: absolute; left: 18px; right: 18px; top: 103px; height: 1px; background: var(--line-grey); }
  .contact-list { position: absolute; left: 18px; top: 116px; list-style: none; }
  .contact-list li { display: flex; align-items: center; height: 19.5px; font-size: 9.5px; }
  .contact-list .icon {
    width: 24px; height: 13px; margin-right: 6px; background: var(--icon-grey); border-radius: 2px;
    display: flex; align-items: center; justify-content: center;
  }
  .address {
    position: absolute; right: 18px; top: 150px; text-align: right; font-size: 9.5px; line-height: 12.5px;
  }

  .card-back {
    position: absolute; left: 480px; top: 875px; width: 356px; height: 209px;
    background: var(--deep-blue);
    display: flex; align-items: center; justify-content: center;
  }
  .card-back .name {
    font-family: "Montserrat", sans-serif; font-weight: 800; font-size: 20px; color: #ffffff; letter-spacing: 0.5px;
  }
</style>
</head>
<body>
<div class="canvas">
  <section class="brochure">
    <div class="brand-mark">
      <span class="badge"></span>
      <span class="name">KESTRELVALE CELLS</span>
    </div>

    <h1 class="headline"><span>OPENING SOON</span></h1>

    <div class="contact-label">CONTACT US</div>

    <div class="card-front">
      <div class="person">DEAN HALLOWAY</div>
      <div class="mini-brand">KESTRELVALE CELLS</div>
      <div class="rule"></div>
      <ul class="contact-list">
        <li><span class="icon"><svg width="8" height="10" viewBox="0 0 8 10"><rect x="1" y="0.5" width="6" height="9" rx="1" fill="none" stroke="#fff"/></svg></span>0400 217 593</li>
        <li><span class="icon"><svg width="10" height="10" viewBox="0 0 10 10"><path d="M2 1l2 2-1 1.5c.8 1.3 1.7 2.2 3 3L7.5 6l2 2-1.5 1.5C5 9 1 5 .5 2z" fill="#fff"/></svg></span>08 9418 2206</li>
        <li><span class="icon"><svg width="10" height="8" viewBox="0 0 10 8"><rect x="0.5" y="0.5" width="9" height="7" fill="none" stroke="#fff"/><path d="M.5 .5l4.5 4 4.5-4" fill="none" stroke="#fff"/></svg></span>dean@kvcells.com.au</li>
        <li><span class="icon"><svg width="10" height="10" viewBox="0 0 10 10"><circle cx="5" cy="5" r="4.3" fill="none" stroke="#fff"/><path d="M.7 5h8.6M5 .7c-2.5 2.5-2.5 6 0 8.6M5 .7c2.5 2.5 2.5 6 0 8.6" fill="none" stroke="#fff" stroke-width=".8"/></svg></span>www.kestrelvalecells.com.au</li>
      </ul>
      <div class="address">Unit 4/7<br>Corvane Loop<br>Harlowe&nbsp; WA&nbsp; 6099</div>
    </div>

    <div class="card-back">
      <span class="name">KESTRELVALE CELLS</span>
    </div>
  </section>
</div>
</body>
</html>
```